Business Card Design Project

Business Card design based on logo.

I need business card, letterhead, envelope, and if possible, Powerpoint slide template.

On front of business card: Just logo- and  my name and title:  Rosalind Pekar, Principal

On reverse-logo and the rest of the contact info:

4857 Orchard Lane
Alder Creek, CA 95710
650-381-2276
rp@brindlestudyworks.example

On letterhead-Just logo at top, at bottom  the rest-very small along the bottom

On PPT slide-just the logo.

I also want to try a few other colors-I like lime/dark grey (not black) but would like to try Sienna, maybe also indigo or bright blue-green.

I forgot to add-

On the business card-switch to vertical on reverse side and put:

Reverse side-switch to vertical and list:

Rosalind Pekar
Principal
Brindle Study Works, LLC

650-381-2276

4857 Orchard Lane
Alder Creek, CA 95710

Rosalind Pekar
Principal

650-381-2276

4857 Orchard Lane
Alder Creek, CA 95710

I have another project at the same time-for Stationery. Feel free to submit to that one also.

That one includes letterhead, envelope, PPT slide, folder cover sheet-RP

Industry/Entity Type

Business

Requirements
Must have
• Must use logo-preferably lime green version-with gray, not black or just 2-tone -logo on colored background.

```html
<!DOCTYPE html>
<html lang="en">
<head>
<meta charset="utf-8">
<title>Brindle Study Works – Business Card</title>
<link rel="stylesheet" href="https://fonts.googleapis.com/css2?family=Cinzel:wght@600&family=Questrial&display=swap">
<style>
  :root {
    --backdrop: #e9e4df;
    --card-white: #ffffff;
    --card-shade: #ececec;
    --ink-dark: #3d3d3d;
    --ink-mid: #555555;
    --gold: #c8960c;
    --gold-bright: #f2c21a;
    --gold-text: #f7d23a;
    --sienna-light: #e3a51a;
    --sienna-mid: #c07a1c;
    --sienna-dark: #8a4524;
  }
  * { box-sizing: border-box; margin: 0; padding: 0; }
  html, body {
    width: 1200px; height: 871px; overflow: hidden;
    background: var(--backdrop);
  }
  .canvas { position: relative; width: 1200px; height: 871px; }
  .card {
    position: absolute; top: 115px;
    width: 366px; height: 640px;
    box-shadow: 0 10px 28px rgba(60, 40, 20, 0.25);
  }

  /* Shared wordmark: one colour, one weight */
  .wordmark {
    display: flex; flex-direction: column; align-items: center; gap: 6px;
    font-family: "Cinzel", serif; font-weight: 600;
    text-transform: uppercase; letter-spacing: 0.16em;
    font-size: 28px; line-height: 1.2; color: var(--ink-dark);
  }
  .wordmark-top { display: flex; align-items: center; gap: 12px; }
  .wordmark-square { width: 16px; height: 16px; background: currentColor; flex: none; }

  /* Contact side */
  .card-contact {
    left: 200px;
    background: radial-gradient(ellipse at 50% 30%, var(--card-white) 45%, var(--card-shade) 100%);
    padding: 92px 30px 0 44px;
  }
  .identity { margin-top: 118px; }
  .person-name {
    font-family: "Cinzel", serif; font-weight: 600;
    font-size: 26px; color: var(--ink-dark); letter-spacing: 0.02em;
    white-space: nowrap;
  }
  .person-title {
    margin-top: 4px;
    font-family: "Questrial", sans-serif; font-size: 19px;
    color: var(--gold); letter-spacing: 0.03em;
  }
  .company {
    margin-top: 6px;
    font-family: "Questrial", sans-serif; font-size: 13px;
    color: var(--ink-mid); letter-spacing: 0.04em; text-transform: uppercase;
  }
  .contact-list { margin-top: 58px; list-style: none; }
  .contact-item {
    display: flex; align-items: flex-start; gap: 16px;
    font-family: "Questrial", sans-serif; font-size: 15px;
    color: var(--ink-mid); margin-bottom: 22px; line-height: 1.35;
    white-space: nowrap;
  }
  .contact-icon { width: 17px; height: 17px; flex: none; margin-top: 1px; fill: var(--gold); }
  .contact-icon-outline { fill: none; stroke: var(--gold); stroke-width: 2; }

  /* Brand side */
  .card-brand {
    left: 634px;
    background: radial-gradient(ellipse at 50% 45%, var(--gold-bright) 0%, var(--sienna-light) 28%, var(--sienna-mid) 58%, var(--sienna-dark) 100%);
    display: flex; align-items: center; justify-content: center;
  }
  .card-brand .wordmark { color: var(--gold-text); font-size: 30px; }
</style>
</head>
<body>
<main class="canvas">
  <section class="card card-contact">
    <div class="wordmark">
      <span class="wordmark-top"><span class="wordmark-square"></span><span>Brindle</span></span>
      <span>Study</span>
    </div>

    <div class="identity">
      <h1 class="person-name">ROSALIND PEKAR</h1>
      <p class="person-title">PRINCIPAL</p>
      <p class="company">Brindle Study Works, LLC</p>
    </div>

    <ul class="contact-list">
      <li class="contact-item">
        <svg class="contact-icon" viewBox="0 0 24 24" aria-hidden="true"><path d="M6.6 10.8a15.1 15.1 0 0 0 6.6 6.6l2.2-2.2a1 1 0 0 1 1-.25 11.4 11.4 0 0 0 3.6.57 1 1 0 0 1 1 1V20a1 1 0 0 1-1 1A17 17 0 0 1 3 4a1 1 0 0 1 1-1h3.5a1 1 0 0 1 1 1c0 1.25.2 2.45.57 3.57a1 1 0 0 1-.25 1z"/></svg>
        <span>650-381-2276</span>
      </li>
      <li class="contact-item">
        <svg class="contact-icon contact-icon-outline" viewBox="0 0 24 24" aria-hidden="true"><path d="M2 6h20v12H2z M2 6l10 7 10-7"/></svg>
        <span>rp@brindlestudyworks.example</span>
      </li>
      <li class="contact-item">
        <svg class="contact-icon" viewBox="0 0 24 24" aria-hidden="true"><path d="M12 3l10 9h-3v9h-5v-6h-4v6H5v-9H2z"/></svg>
        <span>4857 Orchard Lane<br>Alder Creek, CA 95710</span>
      </li>
    </ul>
  </section>

  <section class="card card-brand">
    <div class="wordmark">
      <span class="wordmark-top"><span class="wordmark-square"></span><span>Brindle</span></span>
      <span>Study</span>
    </div>
  </section>
</main>
</body>
</html>
```